New nutrition counseling business needs a flyer and logo design for marketing purposes

Need a new flyer for distribution to advertise and inform the public about new Dietetic Counseling service. The new business name is Harbor of Vitality with “Harbor” being the main name. It will provide nutrition consultation services to individuals who seek to change their dietary habits to achieve a variety of different health objectives. These objectives can include, but are not limited to weight management, enhanced athletic performance, improved health biomarkers, and reducing the risks or symptoms of chronic nutrition related diseases. The services provided include direct one on one counseling that entails health and nutrition assessments, evaluation of goals, and the determination of strategies to meet these goals. We would like to see designs that use an ocean color scheme with purple aspects as well. Color and logo ideas attached in uploads. Please include logo on the flyer as well.

Target Market(s)

General Population

Colors
0094D4
00A9DD
6FCCEA
C7EBF8
E9F6FB
00AB8E
00BBA5
67D7C9
C6EFE9
E9F9F6
6B429C
8869AF
B7A5CE
E3DAEB
F3F0F8

Requirements
Nice to have
• Pictures of nourishing foods, fruits, vegetables etc.
Should not have
• Do not include people in flyer or logo design

```html
<!DOCTYPE html>
<html lang="en">
<head>
<meta charset="utf-8">
<title>Harbor of Vitality – Nutrition Consultation Flyer</title>
<link href="https://fonts.googleapis.com/css2?family=Montserrat:wght@400;500;600;700;800&family=Bebas+Neue&family=Fredoka:wght@500;600&display=swap" rel="stylesheet">
<style>
  :root{
    --teal:#3fcbb9;
    --teal-soft:#5ed6c8;
    --teal-band:#62d8c6;
    --purple:#6a3fa3;
    --purple-deep:#5e3595;
    --sky:#74b8f1;
    --sky-deep:#5ea9ea;
    --green:#8cc963;
    --green-dark:#3c5a25;
    --ink:#222226;
    --navy:#1f2a44;
    --blue-text:#3a7fd0;
    --page:#f2f2f2;
    --white:#ffffff;
  }
  *{margin:0;padding:0;box-sizing:border-box}
  html,body{width:1200px;height:2390px;overflow:hidden;background:var(--page)}
  body{font-family:"Montserrat",sans-serif;color:var(--ink);position:relative}
  .flyer{position:absolute;left:50px;top:483px;width:1100px;height:1424px;background:var(--white);overflow:hidden;box-shadow:0 6px 24px rgba(0,0,0,.12)}
  .abs{position:absolute}
  .backdrop{position:absolute;left:0;top:0;width:1100px;height:1424px}
  .photo{position:absolute}
  .food-photo{left:500px;top:0;width:600px;height:540px;border-radius:0 0 0 300px;background:radial-gradient(circle at 55% 45%,#e9ece6 0%,#cfd8c8 40%,#9fbf7f 70%,#d9d9d6 100%)}
  .fruit-photo{left:300px;top:1060px;width:320px;height:230px;border-radius:40px;background:radial-gradient(circle at 50% 55%,#f0b53d 0%,#e0643a 45%,#8bb34a 80%,rgba(139,179,74,0) 100%)}
  .dumbbell-photo{left:0;top:505px;width:110px;height:250px;border-radius:0 40px 40px 0;background:linear-gradient(160deg,#6cc04a,#3f9a36 60%,#e8d34a)}
  .logo{left:60px;top:70px;display:flex;align-items:center;gap:16px}
  .logo-dot{width:56px;height:56px;border-radius:50%;background:var(--teal)}
  .logo-name{font-weight:700;font-size:44px;color:var(--blue-text);line-height:1}
  .headline{left:58px;top:290px;font-weight:800;font-size:70px;line-height:64px;letter-spacing:-.5px}
  .headline span{display:block}
  .hl-teal{color:var(--teal)}
  .hl-purple{color:var(--purple)}
  .hl-dark{color:var(--ink)}
  .tab{position:absolute;font-weight:600;display:flex;align-items:center;justify-content:center}
  .tab-owner{left:72px;top:534px;width:192px;height:40px;background:#7fdbc9;color:var(--navy);font-size:26px;letter-spacing:1.5px}
  .owner-name{left:128px;top:588px;font-size:42px;color:var(--navy);font-weight:400;letter-spacing:.5px}
  .owner-name b{font-weight:600;color:var(--white)}
  .license-label{left:124px;top:664px;font-size:21px;font-weight:600;color:var(--navy);letter-spacing:3px;line-height:26px}
  .license-pill{left:256px;top:664px;width:212px;height:64px;border-radius:14px;background:var(--purple);color:var(--white);font-size:30px;font-weight:600;letter-spacing:1.5px;display:flex;align-items:center;justify-content:center;border:3px solid var(--white);transform:skewX(-6deg)}
  .tab-green{background:var(--green);color:var(--green-dark);border:3px solid #dff0cf}
  .tab-cred{left:660px;top:570px;width:186px;height:58px;font-size:25px}
  .tab-goal{left:62px;top:792px;width:98px;height:42px;font-size:22px;font-weight:700}
  .tab-serv{left:658px;top:828px;width:148px;height:44px;font-size:24px;font-weight:700}
  .list{position:absolute;list-style:none}
  .list li{position:relative;padding-left:28px}
  .list li::before{content:"";position:absolute;left:0;top:.42em;width:13px;height:13px;border-radius:50%;border:2px solid currentColor;opacity:.85}
  .cred-list{left:658px;top:655px;font-size:18.5px;font-weight:500;color:var(--navy);line-height:32.5px}
  .serv-list{left:660px;top:898px;width:420px;font-size:19px;font-weight:500;color:var(--white);line-height:23px}
  .serv-list li{margin-bottom:18px}
  .serv-list li::before{border-color:var(--sky)}
  .goal-text{left:62px;top:852px;font-size:25px;line-height:29px;color:var(--ink)}
  .goal-text b{font-weight:700}
  .goal-text .accent{color:var(--purple);font-weight:600}
  .modes{left:96px;top:1005px;font-size:21.5px;line-height:26px;font-weight:600;color:var(--ink)}
  .modes .accent{color:var(--blue-text);font-weight:500}
  .chat-text{left:100px;top:1098px;font-family:"Fredoka",sans-serif;line-height:1}
  .chat-lets{font-size:46px;color:var(--purple);font-weight:600;display:block}
  .chat-big{font-size:82px;color:var(--white);font-weight:600;display:block;margin-top:-6px}
  .free{left:60px;top:1332px;font-family:"Bebas Neue",sans-serif;font-size:50px;line-height:1;letter-spacing:-.3px;color:var(--ink);white-space:nowrap}
  .free .blue{color:var(--blue-text)}
  .intro{left:376px;top:1305px;font-size:21.5px;line-height:25px;font-weight:500;color:var(--navy)}
  .divider{left:710px;top:1300px;width:2px;height:96px;background:rgba(255,255,255,.7)}
  .contact{left:736px;top:1306px;font-size:18px;color:var(--navy);font-weight:500}
  .contact-row{display:flex;align-items:center;height:40px}
  .contact-row svg{width:20px;height:20px;margin-right:14px}
  .contact-label{font-size:12.5px;font-weight:700;text-decoration:underline;width:58px}
</style>
</head>
<body>
<main class="flyer">
  <svg class="backdrop" viewBox="0 0 1100 1424" aria-hidden="true">
    <path d="M470 0 C440 200 520 420 760 520 C880 565 1010 560 1100 520 L1100 540 C1000 590 860 590 740 540 C500 440 430 220 450 0 Z" fill="var(--teal)"/>
    <polygon points="0,520 490,520 540,576 1060,570 1100,630 1100,810 570,810 548,758 0,758" fill="var(--sky)"/>
    <path d="M0,1140 C200,1075 420,1105 530,1030 L585,810 L1100,810 L1100,1290 L0,1290 Z" fill="var(--purple)"/>
    <rect x="0" y="1290" width="1100" height="134" fill="var(--white)"/>
    <polygon points="348,1300 1100,1296 1100,1412 348,1412" fill="var(--teal-band)"/>
    <path d="M90,1078 H290 A20 20 0 0 1 310 1098 V1230 A20 20 0 0 1 290 1250 H150 L122,1300 L118,1250 H90 A20 20 0 0 1 70 1230 V1098 A20 20 0 0 1 90 1078 Z" fill="var(--teal-soft)"/>
  </svg>

  <div class="photo food-photo" role="img" aria-label="Photo of meal prep containers filled with vegetables, fruit, rice and salad"></div>
  <div class="photo dumbbell-photo" role="img" aria-label="Photo of a green dumbbell wrapped in a measuring tape"></div>
  <div class="photo fruit-photo" role="img" aria-label="Photo of a basket of assorted fresh fruits and vegetables"></div>

  <div class="abs logo"><span class="logo-dot"></span><span class="logo-name">Harbor of Vitality</span></div>

  <h1 class="abs headline">
    <span class="hl-teal">Nutrition</span>
    <span class="hl-purple">consultation</span>
    <span class="hl-dark">services</span>
  </h1>

  <div class="tab tab-owner">Owner</div>
  <p class="abs owner-name">Marisol <b>Delgado</b></p>
  <p class="abs license-label">License<br>Number</p>
  <div class="abs license-pill">ND 20417</div>

  <div class="tab tab-green tab-cred">Credentials</div>
  <ul class="list cred-list">
    <li>Master of Science in Dietetics and</li>
    <li>Nutrition</li>
    <li>Registered Dietitian (RD)</li>
    <li>Licensed Dietitian Nutritionist (LDN)</li>
  </ul>

  <div class="tab tab-green tab-goal">GOAL</div>
  <p class="abs goal-text">Helping clients foster <b>positive<br>nutrition practices</b> for a<br><span class="accent">healthier lifestyle</span></p>
  <p class="abs modes">Both in <span class="accent">person &amp; virtual<br>consultations</span> are offered</p>

  <div class="tab tab-green tab-serv">SERVICES</div>
  <ul class="list serv-list">
    <li>Medical Nutrition Therapy for chronic conditions such as diabetes, hypertension, high cholesterol, &amp; more</li>
    <li>Weight Management</li>
    <li>Healthy Eating and Meal Planning</li>
    <li>Nutrition for Athletic Performance</li>
    <li>Pre and Post Natal Nutrition</li>
    <li>Personalized meal plans uniquely catered to each individual</li>
    <li>Highly collaborative approach to help you meet your goals</li>
  </ul>

  <p class="abs chat-text"><span class="chat-lets">Let's</span><span class="chat-big">Chat</span></p>

  <p class="abs free"><span class="blue">FREE</span> 15-MINUTE</p>
  <p class="abs intro">introductory consultation to<br>discuss program details<br>and rates</p>
  <div class="abs divider"></div>
  <div class="abs contact">
    <div class="contact-row">
      <svg viewBox="0 0 24 24" aria-hidden="true"><path d="M6.6 10.8a15.1 15.1 0 0 0 6.6 6.6l2.2-2.2c.3-.3.7-.4 1-.2 1.1.4 2.3.6 3.6.6.6 0 1 .4 1 1V20c0 .6-.4 1-1 1A17 17 0 0 1 3 4c0-.6.4-1 1-1h3.5c.6 0 1 .4 1 1 0 1.3.2 2.5.6 3.6.1.3 0 .7-.2 1z" fill="none" stroke="var(--purple)" stroke-width="1.8"/></svg>
      <span class="contact-label">PHONE</span><span>555-014-2278</span>
    </div>
    <div class="contact-row">
      <svg viewBox="0 0 24 24" aria-hidden="true"><rect x="2" y="5" width="20" height="14" rx="1.5" fill="var(--purple)"/><path d="M3 6l9 7 9-7" fill="none" stroke="var(--white)" stroke-width="1.6"/></svg>
      <span class="contact-label">EMAIL:</span><span>Marisol@delgadord.net</span>
    </div>
  </div>
</main>
</body>
</html>
```